Webdesign für islamisches Bestattungsunternehmen
Sehr flexibel, sehr schnell in der Umsetzung als auch der Änderung! Wir werden ihn auf jeden Fall nochmal buchen sobald wir ein neues Projekt haben!
Zielgruppe
islamisches Bestattungsunternehmen, Grabsteine, Grabpflege
Aufgabenstellung
wir wollen ein elegantes design mit einem hauch an exklusivität. wir sind nicht auf billig aus, tatsächlich hochwertig, etwas teurer als die konkurrenz aber dafür bieten wir auch was an.
unser logo haben wir auch hier machen lassen.
www.nurelan-bestattung.eu
LEUTE!
Wir wünschen uns dass direkt auf der ersten seite die 3 optionen sofort ersichtlich sind!!! nicht dass die leute noch runterscrollen müssen...

```html
<!DOCTYPE html>
<html lang="de">
<head>
<meta charset="utf-8">
<title>Nurelan-Bestattung</title>
<link href="https://fonts.googleapis.com/css2?family=Lato:wght@400;700;900&display=swap" rel="stylesheet">
<style>
:root{
  --gold:#e2c53c;
  --gold-dark:#c9a92a;
  --ink:#1d1d1d;
  --page:#262626;
  --bar:#111;
  --panel:#f4f4f4;
  --white:#fff;
  --text:#222;
  --muted:#9a9a9a;
  --red:#e3141b;
}
*{box-sizing:border-box;margin:0;padding:0}
html,body{width:1200px;height:2430px;overflow:hidden}
body{font-family:'Lato',sans-serif;background:var(--page);color:var(--text);position:relative}
.backdrop{position:absolute;inset:0;background:radial-gradient(circle at 50% 30%,#2e2e2e,#1e1e1e)}
.abs{position:absolute}

/* header */
.site-header{position:absolute;left:0;top:0;width:1200px;height:68px;background:var(--bar);border-bottom:3px solid var(--gold)}
.brand{position:absolute;left:151px;top:22px;display:flex;align-items:center;gap:7px;color:var(--gold);font-weight:700;font-size:15px;letter-spacing:.5px}
.brand i{width:10px;height:10px;background:var(--gold);display:block}
.main-nav{position:absolute;right:150px;top:26px;display:flex;gap:38px}
.main-nav a{color:var(--gold);font-size:11.5px;font-weight:700;text-decoration:none;letter-spacing:.2px}

/* hero */
.hero{left:150px;top:107px;width:900px;height:378px;border-radius:8px;background:linear-gradient(120deg,#888 0%,#ccc 55%,#fff 70%,#ddd 100%);padding:14px}
.hero-photo{width:100%;height:100%;border-radius:8px;background:linear-gradient(100deg,#1b0d08 0%,#5a2a1b 25%,#2a1410 45%,#6a3a26 60%,#1a0f0b 80%,#0d0806 100%);position:relative}
.hero-caption{position:absolute;left:245px;top:240px;border-left:4px solid var(--gold);padding-left:12px;color:#fff;font-size:27px;font-weight:700;line-height:32px}
.dots{display:flex;gap:9px;justify-content:center}
.dots span{width:7px;height:7px;border-radius:50%;background:#fff}
.dots span.on{background:var(--gold)}
.hero .dots{position:absolute;left:0;right:0;bottom:20px}

/* service cards */
.service{top:504px;width:287px;height:196px;border-radius:6px;background:linear-gradient(120deg,#888,#ddd 60%,#aaa);padding:7px}
.service-photo{width:100%;height:100%;border-radius:6px;position:relative;overflow:hidden}
.service-photo span{position:absolute;left:0;right:0;bottom:12px;text-align:center;color:#fff;font-size:18px;font-weight:700}
.s1 .service-photo{background:linear-gradient(180deg,#6b5a3a,#2a2218 60%,#141210)}
.s2 .service-photo{background:linear-gradient(180deg,#5d86b8,#8aa0a8 45%,#5d7a45 70%,#2e3a22)}
.s3 .service-photo{background:linear-gradient(180deg,#c7893a,#6b5a3e 40%,#4c6030 70%,#263020)}

/* content sheet */
.sheet{left:150px;top:719px;width:900px;height:1567px;background:var(--white);border-radius:6px 6px 0 0;overflow:hidden}
.about{position:absolute;left:0;top:0;width:900px;height:230px;background:var(--panel);border-bottom:1px solid #ddd}
.about-mark{position:absolute;left:34px;top:95px;width:230px;text-align:center;font-size:22px;font-weight:900;color:var(--ink);letter-spacing:.5px}
.about-body{position:absolute;left:286px;top:31px;width:580px}
.about-body h2{font-size:20px;font-weight:700;color:var(--ink);margin-bottom:16px}
.about-body p{font-size:11px;line-height:15px;margin-bottom:15px;color:#222}

.section-title{position:absolute;left:0;width:900px;text-align:center;font-size:20px;font-weight:700;color:var(--ink)}

.gallery{position:absolute;left:31px;top:316px;width:842px}
.g-row{display:flex;gap:1px;margin-bottom:1px}
.g-row div{height:150px}
.g-row.two div{height:173px}

/* prayers */
.prayer{position:absolute;top:734px;width:268px;height:325px}
.prayer-frame{position:absolute;left:0;top:30px;width:268px;height:295px;border:5px solid var(--gold);border-radius:22px;padding:12px}
.prayer-inner{width:100%;height:100%;border:1px solid #888;border-radius:14px;padding:14px 18px 0}
.prayer-flowers{position:absolute;left:70px;top:0;width:128px;height:52px;border-radius:30px;background:radial-gradient(ellipse,#e79aa5 0%,#f0c4c0 45%,rgba(160,190,150,.6) 70%,transparent 75%)}
.prayer h3{text-align:center;font-size:16px;font-weight:400;color:var(--ink);margin:10px 0 18px}
.prayer p{font-size:11px;line-height:15px;text-align:justify;margin-bottom:14px}
.sheet .dots.dark{position:absolute;left:0;right:0;top:1090px}
.dots.dark span{width:9px;height:9px;background:#444}
.dots.dark span.on{background:var(--gold)}

/* contact */
.contact{position:absolute;left:0;top:1132px;width:900px;height:331px;background:var(--panel);border-top:1px solid #ddd}
.contact-intro{position:absolute;left:48px;top:38px;width:222px}
.contact-intro h2{font-size:20px;font-weight:400;color:var(--ink);margin-bottom:10px}
.contact-intro p{font-size:11px;line-height:15px;padding-left:3px}
.contact-flowers{position:absolute;left:274px;top:35px;width:104px;height:258px;border-radius:50px;background:linear-gradient(180deg,rgba(130,170,130,.5),#e9a7b4 35%,#f2c8c4 60%,rgba(130,170,130,.5))}
.field{position:absolute;height:40px;background:#fff;border:1px solid #ddd;font-size:11px;color:var(--muted);padding:12px 17px}
.field.select::after{content:"";position:absolute;right:18px;top:17px;border:6px solid transparent;border-top:7px solid #777}
.send{position:absolute;left:497px;top:251px;width:243px;height:40px;background:var(--gold);color:var(--ink);font-size:15px;text-align:center;line-height:40px;font-weight:400}

/* call banner */
.call-banner{position:absolute;left:0;top:1463px;width:900px;height:104px;background:linear-gradient(90deg,#4a3018 0%,#2a2420 30%,#1d1b1a 50%,#b5a68b 62%,#bcae92 100%)}
.call-banner .sunset{position:absolute;left:0;top:0;width:520px;height:104px;background:radial-gradient(circle at 80px 55px,#ffd27a 0,#d08a3a 25%,transparent 60%)}
.phone{position:absolute;left:148px;top:26px;display:flex;align-items:center;gap:12px;color:#fff;font-size:32px;font-weight:700}
.catalog{position:absolute;left:508px;top:26px;width:344px;height:46px;background:var(--red);border:2px solid #fff;color:#fff;font-size:23px;font-weight:700;padding:7px 14px}
.pdf{position:absolute;left:780px;top:16px}

/* footer */
.site-footer{position:absolute;left:0;top:2359px;width:1200px;height:71px;background:var(--bar);border-top:3px solid var(--gold)}
.footer-brand{position:absolute;left:151px;top:32px;color:var(--gold);font-size:11px;font-weight:700}
.legal{position:absolute;left:0;right:0;top:33px;text-align:center;font-size:11px;color:var(--gold)}
.legal a{color:var(--gold);text-decoration:none;margin:0 7px}
.copyright{position:absolute;right:150px;top:33px;font-size:11px;color:#ddd}
</style>
</head>
<body>
<div class="backdrop" role="img" aria-label="Dunkles ornamentales Hintergrundmuster"></div>

<header class="site-header">
  <div class="brand"><i></i>NURELAN-BESTATTUNG</div>
  <nav class="main-nav">
    <a href="#">SEITEN 1</a><a href="#">SEITEN 2</a><a href="#">SEITEN 3</a><a href="#">SEITEN 4</a><a href="#">SEITEN 5</a><a href="#">SEITEN 6</a><a href="#">SEITEN 7</a><a href="#">KONTAKT</a>
  </nav>
</header>

<section class="abs hero">
  <div class="hero-photo" role="img" aria-label="Foto: Reihe dunkler Holzsärge">
    <div class="hero-caption">Bestattungen deutschlandweit<br>Überführungen weltweit</div>
    <div class="dots"><span class="on"></span><span></span><span></span><span></span><span></span></div>
  </div>
</section>

<a class="abs service s1" style="left:150px"><div class="service-photo" role="img" aria-label="Foto: Kerzen und weiße Rose bei einer Trauerfeier"><span>Bestattung</span></div></a>
<a class="abs service s2" style="left:456px"><div class="service-photo" role="img" aria-label="Foto: Grabstein auf einem Friedhof"><span>Grabsteine</span></div></a>
<a class="abs service s3" style="left:763px"><div class="service-photo" role="img" aria-label="Foto: Friedhof im Abendlicht"><span>Die Grabpflege</span></div></a>

<main class="abs sheet">
  <section class="about">
    <div class="about-mark">NURELAN-BESTATTUNG</div>
    <div class="about-body">
      <h2>Excepteur sint occaecat cupidatat non proident</h2>
      <p>Lorem ipsum dolor sit amet, consectetur adipiscing elit, sed do eiusmod tempor incididunt ut labore et dolore magna aliqua. Ut enim ad minim veniam, quis nostrud exercitation ullamco laboris nisi ut aliquip ex ea commodo consequat. Duis aute irure dolor in reprehenderit in voluptate velit esse cillum dolore eu fugiat nulla pariatur. Excepteur sint occaecat cupidatat non proident, sunt in culpa qui officia deserunt mollit anim id est laborum.</p>
      <p>Ut enim ad minim veniam, quis nostrud exercitation ullamco laboris nisi ut aliquip ex ea commodo consequat. Duis aute irure dolor in reprehenderit in voluptate velit esse cillum dolore eu fugiat nulla pariatur. Excepteur sint occaecat cupidatat non proident, sunt in culpa qui officia deserunt mollit anim id est laborum.</p>
    </div>
  </section>

  <h2 class="section-title" style="top:265px">Galerie</h2>
  <div class="gallery">
    <div class="g-row">
      <div style="width:333px;background:linear-gradient(180deg,#eee,#a33 50%,#3a3a3a)" role="img" aria-label="Foto: Sarg mit Blumenkränzen"></div>
      <div style="width:227px;background:linear-gradient(180deg,#ccc,#999 60%,#b33)" role="img" aria-label="Foto: Mann am Grab"></div>
      <div style="width:280px;background:linear-gradient(180deg,#5a4a30,#2a2820 60%,#1a1a1a)" role="img" aria-label="Foto: Kerzen und weiße Rose"></div>
    </div>
    <div class="g-row two">
      <div style="width:260px;background:linear-gradient(120deg,#2a2a2a,#c44 40%,#ddd 60%,#b06030)" role="img" aria-label="Foto: Trauernde am Sarg mit Engelsfigur"></div>
      <div style="width:133px;background:linear-gradient(180deg,#3a2a20,#2a1f18)" role="img" aria-label="Foto: Rose auf Erde"></div>
      <div style="width:187px;background:linear-gradient(180deg,#6b8db5,#8a9a8a 45%,#5d7a45)" role="img" aria-label="Foto: Grabstein auf Wiese"></div>
      <div style="width:259px;background:linear-gradient(100deg,#2a2a2a,#444 50%,#c33 80%,#5a2a1a)" role="img" aria-label="Foto: Trauergäste am Sarg"></div>
    </div>
  </div>

  <h2 class="section-title" style="top:697px">Gebete</h2>
  <article class="prayer" style="left:31px">
    <div class="prayer-frame"><div class="prayer-inner">
      <h3>Duis aute irure dolor</h3>
      <p>Duis aute irure dolor in reprehenderit in voluptate velit esse cillum dolore eu fugiat nulla pariatur. Excepteur sint occaecat cupidatat non proident, sunt in culpa qui officia deserunt mollit anim id est laborum.</p>
      <p>Ut enim ad minim veniam, quis nostrud exercitation ullamco laboris nisi ut aliquip ex ea commodo consequat.</p>
    </div></div>
    <div class="prayer-flowers" role="img" aria-label="Blumengesteck-Illustration"></div>
  </article>
  <article class="prayer" style="left:318px">
    <div class="prayer-frame"><div class="prayer-inner">
      <h3>Duis aute irure dolor</h3>
      <p>Duis aute irure dolor in reprehenderit in voluptate velit esse cillum dolore eu fugiat nulla pariatur. Excepteur sint occaecat cupidatat non proident, sunt in culpa qui officia deserunt mollit anim id est laborum.</p>
      <p>Ut enim ad minim veniam, quis nostrud exercitation ullamco laboris nisi ut aliquip ex ea commodo consequat.</p>
    </div></div>
    <div class="prayer-flowers" role="img" aria-label="Blumengesteck-Illustration"></div>
  </article>
  <article class="prayer" style="left:605px">
    <div class="prayer-frame"><div class="prayer-inner">
      <h3>Duis aute irure dolor</h3>
      <p>Duis aute irure dolor in reprehenderit in voluptate velit esse cillum dolore eu fugiat nulla pariatur. Excepteur sint occaecat cupidatat non proident, sunt in culpa qui officia deserunt mollit anim id est laborum.</p>
      <p>Ut enim ad minim veniam, quis nostrud exercitation ullamco laboris nisi ut aliquip ex ea commodo consequat.</p>
    </div></div>
    <div class="prayer-flowers" role="img" aria-label="Blumengesteck-Illustration"></div>
  </article>
  <div class="dots dark"><span class="on"></span><span></span><span></span><span></span><span></span></div>

  <section class="contact">
    <div class="contact-intro">
      <h2>Quis nostrud exercitation</h2>
      <p>Lorem ipsum dolor sit amet, consectetur adipiscing elit, sed do eiusmod tempor incididunt ut labore et dolore magna aliqua. Ut enim ad minim veniam, quis nostrud exercitation ullamco laboris nisi ut aliquip ex ea commodo consequat.</p>
    </div>
    <div class="contact-flowers" role="img" aria-label="Aquarell-Blumenranke"></div>
    <div class="field" style="left:360px;top:41px;width:243px">Name</div>
    <div class="field" style="left:618px;top:41px;width:245px">Email</div>
    <div class="field" style="left:360px;top:94px;width:243px">Phone</div>
    <div class="field select" style="left:619px;top:94px;width:245px">Bestattung</div>
    <div class="field" style="left:360px;top:148px;width:504px;height:90px">Kommentare</div>
    <div class="send">SENDEN</div>
  </section>

  <section class="call-banner">
    <div class="sunset" role="img" aria-label="Foto: Kreuz vor Sonnenuntergang am Meer"></div>
    <div class="phone">
      <svg width="28" height="28" viewBox="0 0 24 24" fill="none" stroke="#fff" stroke-width="1.6"><path d="M5 3h4l2 5-2.5 1.5a11 11 0 0 0 6 6L16 13l5 2v4a2 2 0 0 1-2 2A17 17 0 0 1 3 5a2 2 0 0 1 2-2z"/><path d="M15 3a6 6 0 0 1 6 6M15 6.5a2.5 2.5 0 0 1 2.5 2.5"/></svg>
      0176-48 20 15 63
    </div>
    <div class="catalog">Katalog herunterladen</div>
    <svg class="pdf" width="76" height="80" viewBox="0 0 76 80">
      <path d="M20 6h38l12 12v52H20z" fill="#fff" stroke="#ccc"/>
      <rect x="8" y="20" width="30" height="18" fill="var(--red)"/>
      <text x="12" y="34" font-family="Lato,sans-serif" font-size="12" font-weight="700" fill="#fff">PDF</text>
      <path d="M58 40v26" stroke="var(--red)" stroke-width="5"/>
      <path d="M48 62l10 12 10-12z" fill="var(--red)"/>
    </svg>
  </section>
</main>

<footer class="site-footer">
  <div class="footer-brand">NURELAN-BESTATTUNG</div>
  <div class="legal"><a href="#">Datenschutzerklärung</a>|<a href="#">Haftung</a>|<a href="#">Impressum</a></div>
  <div class="copyright">Copyright Nurelan-Bestattung.eu © 2021</div>
</footer>
</body>
</html>
```